Trade fair PLAMX business card 7” x 5”

PLAMX exhibits on technology-hospitality trade fair in the UK this year. Therefore we are looking for well-designed marketing card (examples are linked in the bottom). The main role of these materials is to attract receivers to visit our website & find out more about PLAMX solutions.
Preferred used colours: white, various blue tints, black.
The front should contain branding & motto (“Modern beverage stocktaking”). Logotypes are attached.
The back should contain:
(value proposition),
Modern technology solution for beverage stocktaking
Accurate & effective stocktaking
Swift measuring with 99% accuracy makes stocktaking significantly quicker and more cost effective (or cost optimising).
Software solution supported with/by hardware tools
PLAMX system is based on universally accessible platforms - smartphones, PCs, and laptops. Your main measuring tool, smart scale, is delivered by PLAMX.
Smart & simple reporting system
Data availability - everywhere, anytime
Useful functions help stock managing at your bar
(call to action),
Find us on plamx-vend.com and try PLAMX with a one-month free trial.
(promo code)
Claim your 50% off discount with above promo code
Marketing card examples:
https://www.vendrilosa.com/Which-startup-has-the-best-brochure-in-terms-of-design-and-content
PLAMX solution was created to help bar owners, bar managers and head bartenders to make their stocktaking process swift & accurate. Therefore, our product is targeting every business which sells portioned beverages.
Information Technology

```html
<!DOCTYPE html>
<html lang="en">
<head>
<meta charset="utf-8">
<title>PLAMX – Trade Fair Card</title>
<link rel="stylesheet" href="https://fonts.googleapis.com/css2?family=Roboto:wght@500;700&family=Roboto+Condensed:wght@700&family=Lato:wght@400;700;900&display=swap">
<style>
  :root {
    --page-bg: #e6e6e4;
    --white: #ffffff;
    --band-indigo: rgba(78, 92, 160, 0.92);
    --teal: #22bfa6;
    --teal-deep: #17a58f;
    --blue-deep: #1450a3;
    --blue-bright: #0a83d6;
    --photo-dark: #3a3a3a;
    --photo-mid: #6c6c6c;
    --photo-light: #d8d8d8;
    --photo-pale: #f0f0f0;
    --logo-blue: #2f8fe0;
    --text-soft: rgba(255, 255, 255, 0.9);
  }
  * { margin: 0; padding: 0; box-sizing: border-box; }
  html, body { width: 1200px; height: 800px; overflow: hidden; }
  body {
    background: var(--page-bg);
    display: flex;
    align-items: center;
    justify-content: center;
    gap: 40px;
    font-family: "Lato", sans-serif;
  }
  .card {
    position: relative;
    width: 560px;
    height: 400px;
    overflow: hidden;
    background: var(--white);
    box-shadow: 0 4px 14px rgba(0, 0, 0, 0.18);
  }

  /* Front */
  .front-photo {
    position: absolute; inset: 0;
    background: radial-gradient(circle at 60% 45%, var(--photo-mid) 0%, var(--photo-dark) 70%);
  }
  .motto-band {
    position: absolute; left: 0; top: 0; width: 100%; height: 72px;
    background: var(--band-indigo);
    border-bottom: 3px solid var(--teal);
    display: flex; align-items: center; justify-content: center;
  }
  .motto {
    font-family: "Roboto", sans-serif;
    font-weight: 700;
    font-size: 33px;
    color: var(--white);
    white-space: nowrap;
  }
  .tagline {
    position: absolute; right: 26px; bottom: 40px;
    text-align: right;
    color: var(--white);
    font-size: 21px;
    line-height: 1.25;
  }
  .tagline .accent { color: var(--teal); font-weight: 900; }
  .brand {
    position: absolute; left: 22px; bottom: 22px;
    display: flex; align-items: center; gap: 10px;
  }
  .brand-mark { width: 34px; height: 34px; background: var(--logo-blue); }
  .brand-name {
    font-weight: 900; font-size: 42px; color: var(--white); letter-spacing: 1px;
  }

  /* Back */
  .back-photo {
    position: absolute; right: 0; top: 0; width: 200px; height: 100%;
    background: linear-gradient(180deg, var(--photo-pale), var(--photo-light));
  }
  .headline-band {
    position: absolute; left: 0; top: 24px; width: 385px; height: 44px;
    background: linear-gradient(90deg, var(--teal-deep), var(--teal));
    border-top-right-radius: 22px;
    display: flex; align-items: center; padding-left: 22px;
  }
  .headline {
    font-family: "Roboto Condensed", sans-serif;
    font-weight: 700; font-size: 15.5px; color: var(--white);
    white-space: nowrap;
  }
  .value-panel {
    position: absolute; left: 0; top: 68px; width: 385px; height: 314px;
    background: linear-gradient(135deg, var(--blue-deep), var(--blue-bright));
    border-bottom-right-radius: 26px;
    padding: 14px 22px 0;
    color: var(--white);
  }
  .benefit { margin-bottom: 9px; }
  .benefit-title { font-weight: 900; font-size: 13px; letter-spacing: 0.2px; margin-bottom: 2px; }
  .benefit-text { font-size: 11.5px; line-height: 1.3; color: var(--text-soft); }
  .call-to-action {
    font-size: 12px; line-height: 1.3; font-weight: 700;
    margin-bottom: 8px;
  }
  .promo { display: flex; align-items: center; gap: 12px; }
  .promo-code {
    flex: none;
    background: var(--white); color: var(--blue-deep);
    font-weight: 900; font-size: 14px; letter-spacing: 1px;
    padding: 5px 10px; border-radius: 4px;
  }
  .promo-text { font-size: 11px; line-height: 1.25; color: var(--text-soft); }
</style>
</head>
<body>
  <section class="card card-front">
    <div class="front-photo" role="img" aria-label="Black-and-white photo of a smiling bartender shaking a cocktail behind a bar"></div>
    <div class="motto-band"><h1 class="motto">“Modern Beverage Stocktaking”</h1></div>
    <p class="tagline">Stocktaking made <span class="accent">easy</span><br>https://plamx-vend.com</p>
    <div class="brand"><span class="brand-mark"></span><span class="brand-name">PLAMX</span></div>
  </section>

  <section class="card card-back">
    <div class="back-photo" role="img" aria-label="Black-and-white photo of a man in a suit using a smartphone"></div>
    <div class="headline-band"><h2 class="headline">Modern Technology Solution For Beverage Stocktaking</h2></div>
    <div class="value-panel">
      <div class="benefit">
        <h3 class="benefit-title">ACCURATE &amp; EFFECTIVE STOCKTAKING</h3>
        <p class="benefit-text">Swift measuring with 99% accuracy makes stocktaking significantly quicker &amp; more cost effective.</p>
      </div>
      <div class="benefit">
        <h3 class="benefit-title">SOFTWARE SUPPORTED BY HARDWARE TOOLS</h3>
        <p class="benefit-text">PLAMX system is based on universally accessible platforms – smartphones, PCs and laptops. Your main measuring tool, smart scale, is delivered by PLAMX.</p>
      </div>
      <div class="benefit">
        <h3 class="benefit-title">SMART &amp; SIMPLE REPORTING SYSTEM</h3>
        <p class="benefit-text">Data availability – everywhere, anytime. Useful functions help stock managing at your bar.</p>
      </div>
      <p class="call-to-action">Find us on plamx-vend.com and try PLAMX with a one-month free trial.</p>
      <div class="promo">
        <span class="promo-code">PLAMX50</span>
        <p class="promo-text">Claim your 50% off discount<br>with above promo code</p>
      </div>
    </div>
  </section>
</body>
</html>
```